Exciting new aperitif brand needs a great label

Vel-Doro is a wonderful rich new premium-priced bitter aperitif, with a deep red colour, from a 100+ year old distillery (1890) near Turin in the Piedmont region of Italy. Inspired by Tessoli, it is perfectly formulated to elevate the classic Negroni cocktail (and variations on it). It also goes perfectly in a Spritz or a long mixed drink with soda or tonic. The name Vel-Doro is derived from the French for 'peak' and the Italian word for 'love'.

The label, which should take inspiration from Tessoli, but be distinctively different, can incoporate any number of premium label embellishments (foil, embossing, textures etc) and should be no greater than 11cm (height) x 9cm (width) with any core imagery restricted to a width of c.7cm.

The attached mood board should act as inspiration and colour should largely be restricted to reds, blues, whites and perhaps orange. For completeness, the label should note that the ABV is 25% and the bottle size 70cl.

Target Market(s)

21-45yr olds - equal split female/male

Colors
0054AA
0677BA
7BADD7
CADEEF
E8F1F8
0094D4
00A9DD
6FCCEA
C7EBF8
E9F6FB
EE7325
F08F49
F5BC92
FAE3D3
FDF4ED
EB3D1F
EC4F4E
F09395
F8D3D4
FCEDEE

Requirements
Must have
• Great lettering design on the name Vel-Doro

```html
<!DOCTYPE html>
<html lang="en">
<head>
<meta charset="utf-8">
<title>Vel-Doro Aperitivo – Label Variants</title>
<link rel="stylesheet" href="https://fonts.googleapis.com/css2?family=Cinzel:wght@700;900&family=Leckerli+One&family=Alegreya:wght@700&family=Crimson+Pro:wght@500&display=swap">
<style>
  :root {
    --stage: #000000;
    --paper: #dcebf8;
    --navy: #0c2f6b;
    --navy-deep: #0b1632;
    --gold: #f5b400;
    --gold-light: #ffd24a;
    --red: #d9261c;
    --ink: #0d2a57;
    --white: #ffffff;
    --vine-red: #a8322a;
    --vine-green: #1f6b35;
  }
  html, body {
    margin: 0;
    width: 1200px;
    height: 727px;
    overflow: hidden;
    background: var(--stage);
  }
  .canvas {
    position: relative;
    width: 1200px;
    height: 727px;
  }
  .label {
    position: absolute;
    top: 27px;
    width: 534px;
    height: 653px;
    display: block;
  }
  .label--classic { left: 37px; }
  .label--gilded { left: 604px; }
  .paper { fill: var(--paper); }
  .frame-line { fill: none; stroke: var(--gold); stroke-width: 2.5; }
  .region-name {
    font-family: "Cinzel", serif;
    font-weight: 700;
    font-size: 18px;
    letter-spacing: 1.5px;
    fill: var(--gold);
  }
  .brand-name {
    font-family: "Cinzel", serif;
    font-weight: 900;
    fill: var(--white);
  }
  .since {
    font-family: "Cinzel", serif;
    font-weight: 700;
    font-size: 17px;
    letter-spacing: 5px;
    fill: var(--gold);
  }
  .style-script {
    font-family: "Leckerli One", cursive;
    font-size: 44px;
  }
  .style-script--halo { fill: var(--gold); stroke: var(--gold); stroke-width: 9; stroke-linejoin: round; }
  .style-script--face { fill: var(--white); stroke: var(--navy-deep); stroke-width: 2; paint-order: stroke; }
  .tagline {
    font-family: "Alegreya", serif;
    font-weight: 700;
    font-size: 10.5px;
    fill: var(--white);
  }
  .origin-small, .origin-large {
    font-family: "Cinzel", serif;
    font-weight: 700;
    fill: var(--white);
  }
  .origin-small { font-size: 11px; letter-spacing: 2.5px; }
  .origin-large { font-size: 21px; letter-spacing: 3px; }
  .spec {
    font-family: "Crimson Pro", serif;
    font-weight: 500;
    font-size: 25px;
    fill: var(--ink);
  }
  .stripe { stroke: var(--gold); stroke-width: 3.2; }
</style>
</head>
<body>
<main class="canvas">

  <!-- Variant A: classic with figure panels, red origin badge -->
  <svg class="label label--classic" viewBox="0 0 534 653" xmlns="http://www.w3.org/2000/svg">
    <defs>
      <radialGradient id="navyGlowA" cx="50%" cy="45%" r="60%">
        <stop offset="0" stop-color="#0e3d82"/>
        <stop offset="1" stop-color="#0b1632"/>
      </radialGradient>
      <linearGradient id="goldFadeA" x1="0" y1="0" x2="0" y2="1">
        <stop offset="0" stop-color="#f5b400" stop-opacity="0.75"/>
        <stop offset="1" stop-color="#c78f00" stop-opacity="0.45"/>
      </linearGradient>
      <linearGradient id="vineA" x1="0" y1="0" x2="0" y2="1">
        <stop offset="0" stop-color="#1f6b35"/>
        <stop offset="0.5" stop-color="#a8322a"/>
        <stop offset="1" stop-color="#1f6b35"/>
      </linearGradient>
    </defs>

    <rect class="paper" width="534" height="653"/>

    <!-- upper crest panel -->
    <polygon points="30,26 504,26 432,218 106,218" fill="url(#navyGlowA)"/>
    <polygon class="frame-line" points="30,26 504,26 432,218 106,218"/>
    <rect x="87" y="40" width="359" height="10" rx="5" fill="url(#goldFadeA)" role="img" aria-label="Gold bead-chain ornament rule"/>
    <rect x="105" y="56" width="116" height="133" rx="30" fill="url(#goldFadeA)" role="img" aria-label="Gold acanthus scroll ornament"/>
    <rect x="313" y="56" width="114" height="133" rx="30" fill="url(#goldFadeA)" role="img" aria-label="Gold acanthus scroll ornament"/>
    <g class="flag">
      <rect x="222" y="65" width="87" height="60" fill="none" stroke="var(--gold)" stroke-width="2.5"/>
      <rect x="228" y="71" width="75" height="48" fill="var(--red)"/>
      <rect x="228" y="89" width="75" height="12" fill="var(--white)"/>
      <rect x="259" y="71" width="13" height="48" fill="var(--white)"/>
      <rect x="240" y="71" width="51" height="5" fill="#1d3f8f"/>
    </g>
    <text class="region-name" x="267" y="162" text-anchor="middle">PIEDMONT</text>

    <!-- lower pennant -->
    <polygon points="179,403 354,403 266,631" fill="url(#navyGlowA)"/>
    <polygon class="frame-line" points="179,403 354,403 266,631"/>

    <!-- name band -->
    <rect x="0" y="218" width="534" height="185" fill="url(#navyGlowA)"/>
    <path d="M150,218 C190,218 200,198 267,198 C334,198 344,218 384,218 L384,403 C344,403 334,423 267,423 C200,423 190,403 150,403 Z" fill="url(#navyGlowA)"/>
    <g class="band-stripes">
      <line class="stripe" x1="0" y1="232" x2="150" y2="232"/>
      <line class="stripe" x1="0" y1="243" x2="60" y2="243"/>
      <line class="stripe" x1="0" y1="254" x2="130" y2="254"/>
      <line class="stripe" x1="0" y1="265" x2="40" y2="265"/>
      <line class="stripe" x1="0" y1="276" x2="95" y2="276"/>
      <line class="stripe" x1="0" y1="287" x2="30" y2="287"/>
      <line class="stripe" x1="0" y1="298" x2="80" y2="298"/>
      <line class="stripe" x1="0" y1="309" x2="45" y2="309"/>
      <line class="stripe" x1="0" y1="320" x2="70" y2="320"/>
      <line class="stripe" x1="0" y1="331" x2="35" y2="331"/>
      <line class="stripe" x1="0" y1="342" x2="90" y2="342"/>
      <line class="stripe" x1="0" y1="353" x2="50" y2="353"/>
      <line class="stripe" x1="0" y1="364" x2="120" y2="364"/>
      <line class="stripe" x1="0" y1="375" x2="60" y2="375"/>
      <line class="stripe" x1="0" y1="386" x2="145" y2="386"/>
      <line class="stripe" x1="534" y1="232" x2="384" y2="232"/>
      <line class="stripe" x1="534" y1="243" x2="474" y2="243"/>
      <line class="stripe" x1="534" y1="254" x2="404" y2="254"/>
      <line class="stripe" x1="534" y1="265" x2="494" y2="265"/>
      <line class="stripe" x1="534" y1="276" x2="439" y2="276"/>
      <line class="stripe" x1="534" y1="287" x2="504" y2="287"/>
      <line class="stripe" x1="534" y1="298" x2="454" y2="298"/>
      <line class="stripe" x1="534" y1="309" x2="489" y2="309"/>
      <line class="stripe" x1="534" y1="320" x2="464" y2="320"/>
      <line class="stripe" x1="534" y1="331" x2="499" y2="331"/>
      <line class="stripe" x1="534" y1="342" x2="444" y2="342"/>
      <line class="stripe" x1="534" y1="353" x2="484" y2="353"/>
      <line class="stripe" x1="534" y1="364" x2="414" y2="364"/>
      <line class="stripe" x1="534" y1="375" x2="474" y2="375"/>
      <line class="stripe" x1="534" y1="386" x2="389" y2="386"/>
    </g>
    <path d="M0,218 L150,218 C190,218 200,198 267,198 C334,198 344,218 384,218 L534,218" fill="none" stroke="var(--gold)" stroke-width="3"/>
    <path d="M0,224 L150,224 C190,224 200,205 267,205 C334,205 344,224 384,224 L534,224" fill="none" stroke="var(--gold)" stroke-width="1.2"/>
    <path d="M0,403 L150,403 C190,403 200,423 267,423 C334,423 344,403 384,403 L534,403" fill="none" stroke="var(--gold)" stroke-width="3"/>
    <path d="M0,397 L150,397 C190,397 200,416 267,416 C334,416 344,397 384,397 L534,397" fill="none" stroke="var(--gold)" stroke-width="1.2"/>

    <rect x="236" y="221" width="62" height="37" rx="6" fill="var(--gold)" role="img" aria-label="Gold crown emblem"/>
    <text class="brand-name" x="267" y="346" text-anchor="middle" textLength="432" lengthAdjust="spacingAndGlyphs"><tspan font-size="98">V</tspan><tspan font-size="78">EL-</tspan><tspan font-size="98">D</tspan><tspan font-size="78">ORO</tspan></text>
    <path id="sinceArcA" d="M180,366 Q267,404 354,366" fill="none"/>
    <text class="since" text-anchor="middle"><textPath href="#sinceArcA" startOffset="50%">Since 1890</textPath></text>

    <!-- style and origin -->
    <text class="style-script style-script--halo" x="273" y="475" text-anchor="middle">Aperitivo</text>
    <text class="style-script style-script--face" x="273" y="475" text-anchor="middle">Aperitivo</text>
    <text class="tagline" x="266" y="503" text-anchor="middle">premium-priced</text>
    <text class="tagline" x="266" y="516" text-anchor="middle">bitter</text>
    <rect x="259" y="533" width="14" height="14" fill="var(--gold)" transform="rotate(45 266 540)" role="img" aria-label="Small gold knot ornament"/>
    <rect x="189" y="559" width="155" height="48" fill="var(--red)" stroke="var(--gold)" stroke-width="2.5"/>
    <rect x="193" y="563" width="147" height="40" fill="none" stroke="var(--white)" stroke-width="0.8"/>
    <text class="origin-small" x="266" y="580" text-anchor="middle">PRODUCED BY</text>
    <text class="origin-large" x="266" y="601" text-anchor="middle">ITALY</text>

    <rect x="18" y="415" width="100" height="181" rx="18" fill="url(#vineA)" opacity="0.85" role="img" aria-label="Illustration of a robed figure holding up a flowering vine"/>
    <rect x="415" y="415" width="100" height="181" rx="18" fill="url(#vineA)" opacity="0.85" role="img" aria-label="Mirrored illustration of a robed figure holding up a flowering vine"/>

    <text class="spec" x="24" y="628">25% vol.</text>
    <text class="spec" x="510" y="628" text-anchor="end">700 ml.</text>
  </svg>

  <!-- Variant B: gilded scrolls, navy origin badge -->
  <svg class="label label--gilded" viewBox="0 0 534 653" xmlns="http://www.w3.org/2000/svg">
    <defs>
      <radialGradient id="navyGlowB" cx="50%" cy="45%" r="60%">
        <stop offset="0" stop-color="#0e3d82"/>
        <stop offset="1" stop-color="#0b1632"/>
      </radialGradient>
      <linearGradient id="goldFadeB" x1="0" y1="0" x2="0" y2="1">
        <stop offset="0" stop-color="#f5b400" stop-opacity="0.75"/>
        <stop offset="1" stop-color="#c78f00" stop-opacity="0.45"/>
      </linearGradient>
      <linearGradient id="scrollB" x1="0" y1="0" x2="0" y2="1">
        <stop offset="0" stop-color="#ffd24a"/>
        <stop offset="1" stop-color="#e8a400"/>
      </linearGradient>
    </defs>

    <rect class="paper" width="534" height="653"/>

    <polygon points="30,26 504,26 432,218 106,218" fill="url(#navyGlowB)"/>
    <polygon class="frame-line" points="30,26 504,26 432,218 106,218"/>
    <rect x="146" y="33" width="241" height="25" rx="10" fill="url(#goldFadeB)" role="img" aria-label="Gold leaf crest ornament"/>
    <rect x="105" y="56" width="116" height="133" rx="30" fill="url(#goldFadeB)" role="img" aria-label="Gold acanthus scroll ornament"/>
    <rect x="313" y="56" width="114" height="133" rx="30" fill="url(#goldFadeB)" role="img" aria-label="Gold acanthus scroll ornament"/>
    <g class="flag">
      <rect x="222" y="65" width="87" height="60" fill="none" stroke="var(--gold)" stroke-width="2.5"/>
      <rect x="228" y="71" width="75" height="48" fill="var(--red)"/>
      <rect x="228" y="89" width="75" height="12" fill="var(--white)"/>
      <rect x="259" y="71" width="13" height="48" fill="var(--white)"/>
      <rect x="240" y="71" width="51" height="5" fill="#1d3f8f"/>
    </g>
    <text class="region-name" x="267" y="162" text-anchor="middle">PIEDMONT</text>

    <polygon points="179,403 354,403 266,631" fill="url(#navyGlowB)"/>
    <polygon class="frame-line" points="179,403 354,403 266,631"/>

    <rect x="0" y="218" width="534" height="185" fill="url(#navyGlowB)"/>
    <path d="M150,218 C190,218 200,198 267,198 C334,198 344,218 384,218 L384,403 C344,403 334,423 267,423 C200,423 190,403 150,403 Z" fill="url(#navyGlowB)"/>
    <g class="band-stripes">
      <line class="stripe" x1="0" y1="232" x2="150" y2="232"/>
      <line class="stripe" x1="0" y1="243" x2="60" y2="243"/>
      <line class="stripe" x1="0" y1="254" x2="130" y2="254"/>
      <line class="stripe" x1="0" y1="265" x2="40" y2="265"/>
      <line class="stripe" x1="0" y1="276" x2="95" y2="276"/>
      <line class="stripe" x1="0" y1="287" x2="30" y2="287"/>
      <line class="stripe" x1="0" y1="298" x2="80" y2="298"/>
      <line class="stripe" x1="0" y1="309" x2="45" y2="309"/>
      <line class="stripe" x1="0" y1="320" x2="70" y2="320"/>
      <line class="stripe" x1="0" y1="331" x2="35" y2="331"/>
      <line class="stripe" x1="0" y1="342" x2="90" y2="342"/>
      <line class="stripe" x1="0" y1="353" x2="50" y2="353"/>
      <line class="stripe" x1="0" y1="364" x2="120" y2="364"/>
      <line class="stripe" x1="0" y1="375" x2="60" y2="375"/>
      <line class="stripe" x1="0" y1="386" x2="145" y2="386"/>
      <line class="stripe" x1="534" y1="232" x2="384" y2="232"/>
      <line class="stripe" x1="534" y1="243" x2="474" y2="243"/>
      <line class="stripe" x1="534" y1="254" x2="404" y2="254"/>
      <line class="stripe" x1="534" y1="265" x2="494" y2="265"/>
      <line class="stripe" x1="534" y1="276" x2="439" y2="276"/>
      <line class="stripe" x1="534" y1="287" x2="504" y2="287"/>
      <line class="stripe" x1="534" y1="298" x2="454" y2="298"/>
      <line class="stripe" x1="534" y1="309" x2="489" y2="309"/>
      <line class="stripe" x1="534" y1="320" x2="464" y2="320"/>
      <line class="stripe" x1="534" y1="331" x2="499" y2="331"/>
      <line class="stripe" x1="534" y1="342" x2="444" y2="342"/>
      <line class="stripe" x1="534" y1="353" x2="484" y2="353"/>
      <line class="stripe" x1="534" y1="364" x2="414" y2="364"/>
      <line class="stripe" x1="534" y1="375" x2="474" y2="375"/>
      <line class="stripe" x1="534" y1="386" x2="389" y2="386"/>
    </g>
    <path d="M0,218 L150,218 C190,218 200,198 267,198 C334,198 344,218 384,218 L534,218" fill="none" stroke="var(--gold)" stroke-width="3"/>
    <path d="M0,224 L150,224 C190,224 200,205 267,205 C334,205 344,224 384,224 L534,224" fill="none" stroke="var(--gold)" stroke-width="1.2"/>
    <path d="M0,403 L150,403 C190,403 200,423 267,423 C334,423 344,403 384,403 L534,403" fill="none" stroke="var(--gold)" stroke-width="3"/>
    <path d="M0,397 L150,397 C190,397 200,416 267,416 C334,416 344,397 384,397 L534,397" fill="none" stroke="var(--gold)" stroke-width="1.2"/>

    <rect x="236" y="221" width="62" height="37" rx="6" fill="var(--gold)" role="img" aria-label="Gold crown emblem"/>
    <text class="brand-name" x="267" y="346" text-anchor="middle" textLength="432" lengthAdjust="spacingAndGlyphs"><tspan font-size="98">V</tspan><tspan font-size="78">EL-</tspan><tspan font-size="98">D</tspan><tspan font-size="78">ORO</tspan></text>
    <path id="sinceArcB" d="M180,366 Q267,404 354,366" fill="none"/>
    <text class="since" text-anchor="middle"><textPath href="#sinceArcB" startOffset="50%">Since 1890</textPath></text>

    <text class="style-script style-script--halo" x="273" y="475" text-anchor="middle">Aperitivo</text>
    <text class="style-script style-script--face" x="273" y="475" text-anchor="middle">Aperitivo</text>
    <text class="tagline" x="266" y="503" text-anchor="middle">premium-priced</text>
    <text class="tagline" x="266" y="516" text-anchor="middle">bitter</text>
    <rect x="259" y="533" width="14" height="14" fill="var(--gold)" transform="rotate(45 266 540)" role="img" aria-label="Small gold knot ornament"/>
    <rect x="189" y="559" width="155" height="48" fill="var(--navy-deep)" stroke="var(--gold)" stroke-width="2.5"/>
    <rect x="193" y="563" width="147" height="40" fill="none" stroke="var(--white)" stroke-width="0.8"/>
    <text class="origin-small" x="266" y="580" text-anchor="middle">PRODUCED BY</text>
    <text class="origin-large" x="266" y="601" text-anchor="middle">ITALY</text>

    <rect x="11" y="410" width="146" height="196" rx="30" fill="url(#scrollB)" opacity="0.7" role="img" aria-label="Gold baroque scroll ornament"/>
    <rect x="377" y="410" width="146" height="196" rx="30" fill="url(#scrollB)" opacity="0.7" role="img" aria-label="Mirrored gold baroque scroll ornament"/>

    <text class="spec" x="24" y="628">25% vol.</text>
    <text class="spec" x="510" y="628" text-anchor="end">700 ml.</text>
  </svg>

</main>
</body>
</html>
```